Training Brochure for Local Government Program needs a makeover and some creative design!

We would like our plain and boring brochure updated to be enticing for people to register for this program. Our organisation works in Local Government (Councils) in Australia and we are running our "leadership" program again in 2017.

We would like the brochure for this program to be engaging, bright and modern to entice the future leaders to participate.

The original file was created in Publisher, however we require the final file to be an easily editable PDF with front and back cover for updating in future years and for minor content changes.

It is not intended that this will be printed but made available electronically, however A4 size would be appreciated.

We require the following to be included
Our Logo (Supplied)
KWEN Logo (To be supplied within 48 hours)

Target Market(s)

Aspiring Leaders in Government
Young business minded people

Industry/Entity Type

Government

Font styles to use
Serif
Sans Serif
Decorative

Colors

Designer to choose colors to be used in the design.

Requirements
Must have
• Our Logo - Supplied
• The Facilitators logo (KWEN) - Supplied
Nice to have
• Our Corporate colours used
• Some nice photo's or use of icons etc

```html
<!DOCTYPE html>
<html lang="en">
<head>
<meta charset="utf-8">
<title>Emerging Leaders Program Brochure Spread</title>
<link href="https://fonts.googleapis.com/css2?family=Montserrat:wght@300;400;600;700&display=swap" rel="stylesheet">
<style>
  :root {
    --backdrop: #5b5b5a;
    --paper: #fbfbfa;
    --ink: #5a5a5a;
    --rust: #b5521f;
    --amber: #e0a522;
    --gold: #e7b73a;
    --forest: #1d5a3c;
    --forest-deep: #0f3322;
    --white: #ffffff;
  }
  * { box-sizing: border-box; margin: 0; padding: 0; }
  html, body { width: 1200px; height: 700px; overflow: hidden; }
  body {
    background: var(--backdrop);
    font-family: "Montserrat", sans-serif;
    display: flex; align-items: center; justify-content: center;
  }
  .spread { display: flex; width: 1180px; height: 418px; box-shadow: 0 10px 30px rgba(0,0,0,.35); }
  .page { width: 590px; height: 418px; position: relative; overflow: hidden; }

  /* Left page */
  .page-left { background: var(--paper); display: flex; }
  .sidebar {
    width: 138px; height: 100%; flex: none;
    background: linear-gradient(180deg, var(--rust) 0%, #c2661d 45%, var(--amber) 100%);
    color: var(--white); font-weight: 300; font-size: 8.6px; line-height: 1.42;
    padding: 40px 14px 14px 22px;
  }
  .content { width: 452px; padding: 18px 24px 10px 28px; color: var(--ink); font-size: 7.4px; line-height: 1.32; font-weight: 400; }
  .intro { margin-bottom: 6px; }
  .columns { display: flex; gap: 14px; }
  .columns > section { flex: 1; }
  .section-title { color: var(--rust); font-weight: 400; font-size: 12px; margin-bottom: 2px; }
  .objectives ul { list-style: none; }
  .objectives li { padding-left: 7px; position: relative; }
  .objectives li::before { content: "•"; position: absolute; left: 0; }
  .program-details p + p { margin-top: 5px; }
  strong { font-weight: 700; }

  .fee { position: relative; width: 400px; height: 72px; margin: 4px 0 4px; }
  .fee svg { position: absolute; left: 0; top: 0; }
  .fee-title { position: absolute; left: 178px; top: 34px; color: var(--white); font-size: 11px; line-height: 1; }
  .fee-member { position: absolute; left: 10px; top: 43px; color: var(--white); font-size: 6.6px; line-height: 1.15; }
  .fee-member b { display: block; font-size: 9px; margin-bottom: 2px; }
  .fee-non { position: absolute; right: 8px; top: 0; font-size: 7px; line-height: 1.15; text-align: right; }
  .fee-non b { color: var(--amber); font-size: 9px; display: block; }
  .footnote { font-size: 5.6px; line-height: 1.3; margin-bottom: 5px; }
  .includes ul { list-style: none; }
  .includes li::before { content: "• "; color: var(--amber); }

  /* Right page */
  .page-right { color: var(--white); }
  .venue-photo {
    position: absolute; inset: 0;
    background: radial-gradient(ellipse at 40% 55%, #2f6a48 0%, var(--forest) 40%, var(--forest-deep) 100%);
  }
  .right-content { position: relative; padding: 30px 30px 20px 32px; font-size: 7.6px; line-height: 1.4; }
  .right-content .section-title { color: var(--white); }
  .right-content p { margin-bottom: 6px; }
  .info-row { display: flex; gap: 10px; margin-top: 30px; }
  .info { flex: 1; text-align: center; font-size: 7.2px; line-height: 1.35; }
  .info svg { display: block; margin: 0 auto 6px; }
  .info h3 { font-size: 7.4px; font-weight: 700; text-transform: uppercase; margin-bottom: 2px; }
</style>
</head>
<body>
  <div class="spread">
    <article class="page page-left">
      <aside class="sidebar">
        This Program facilitated by the Southern Isle University, is a unique professional development opportunity for current leaders, to positions of leadership and those who aspire to provide leadership in a particular area of interest within the Local Government sector. The Program will focus on equipping emerging leaders with an understanding of the key challenges facing local government in the future, the skills and competencies to develop leadership ability, and the resources to continue learning and practicing leadership behaviours.
      </aside>
      <div class="content">
        <p class="intro">Civic Leaders Tasmania, in conjunction with KWEN Institute for Regional Development, Southern Isle University, is pleased to offer the <strong><em>Emerging Leaders Program</em></strong> once again in 2017.</p>
        <div class="columns">
          <section class="objectives">
            <h2 class="section-title">Objectives</h2>
            <p>The objectives of the program are as follows:</p>
            <ul>
              <li>Develop leadership skills and behaviours for people who will lead at all levels in Local Government.</li>
              <li>Provide an opportunity for participants to network with emerging leaders from different professions to build stronger links and understanding between professions.</li>
              <li>Increase appreciation of the wider challenges facing Local Government and how to respond to them.</li>
              <li>Develop a network of emerging leaders and coaches/mentors to support their development.</li>
              <li>Retain emerging leaders within the Local Government sector.</li>
            </ul>
          </section>
          <section class="program-details">
            <h2 class="section-title">Program Details</h2>
            <p>The Program will be held on <strong>Thursday 30th November and Friday 1st December</strong> at The Riverbank Hotel, Launceston, commencing at 10.00 am to enable travel on Thursday morning.</p>
            <p>The workshops will be facilitated by <strong>Professor Daniel Avery</strong> Professor of Management and Innovation, <strong>Dr Samuel Finch</strong> Lecturer in the Southern School of Business and Economics and <strong>Colin Harper</strong> Coursework Coordinator in the Institute for Regional Development. All have extensive experience in working with local governments locally and internationally. The workshops will be interactive using local government case material from Tasmania and internationally.</p>
          </section>
        </div>
        <div class="fee">
          <svg width="400" height="72" viewBox="0 0 400 72" aria-hidden="true">
            <polygon points="0,40 400,20 400,30 0,72" fill="var(--gold)"/>
          </svg>
          <span class="fee-title">Program Fee</span>
          <span class="fee-member"><b>$990.00*</b>Civic Leaders Tasmania Members</span>
          <span class="fee-non"><b>$1,375.00*</b>Non-Members **</span>
        </div>
        <p class="footnote">*GST Inclusive<br>** Member rates are only available to current financial members only. Non Members are invited to apply for membership prior to registering to access the discounted rate and receive ongoing communication and networking benefits of our association.</p>
        <div class="includes">
          <p>The fee includes:</p>
          <ul>
            <li>Morning teas, lunches and afternoon teas during the program</li>
            <li>Continuous Tea and coffee availability</li>
            <li>Dinner on Thursday night (not including drinks)</li>
            <li>Course materials</li>
            <li>Certificate of Completion</li>
          </ul>
        </div>
      </div>
    </article>

    <article class="page page-right">
      <div class="venue-photo" role="img" aria-label="Photo of the hotel venue building among trees, tinted deep green"></div>
      <div class="right-content">
        <h2 class="section-title">Selection Process</h2>
        <p>Applications for the <strong>Emerging Leaders Program</strong> are invited by completion of the Application Form to be received no later than Friday 10th November 2017 or alternatively by registering electronically on our website here.</p>
        <p>Places are limited for this event and applicants will be accepted on a first in first served basis. Should spaces be unavailable applicants will be placed on a waiting list for the next available space and course.</p>
        <p>It is anticipated that a mix of professions, Council sizes and locations will be represented in the participants. There are no age restrictions for selection to the Program.</p>
        <p><strong>Application forms should be forwarded to Amelia Joyce</strong><br>events@civicleaderstas.org.au</p>

        <div class="info-row">
          <div class="info">
            <svg width="44" height="44" viewBox="0 0 44 44" aria-hidden="true"><circle cx="22" cy="22" r="20" fill="none" stroke="#fff" stroke-width="1.3"/><path d="M22 32 C16 24 15 21 15 18 a7 7 0 0 1 14 0 c0 3 -1 6 -7 14z" fill="none" stroke="#fff" stroke-width="1.3"/><circle cx="22" cy="18" r="2.5" fill="none" stroke="#fff" stroke-width="1.3"/></svg>
            <h3>Venue</h3>
            This program will be held at The Riverbank Hotel Launceston, Cnr Elm and Grove Street, Launceston.
          </div>
          <div class="info">
            <svg width="44" height="44" viewBox="0 0 44 44" aria-hidden="true"><circle cx="22" cy="22" r="20" fill="none" stroke="#fff" stroke-width="1.3"/><circle cx="22" cy="22" r="8" fill="none" stroke="#fff" stroke-width="1.3"/><line x1="10" y1="13" x2="10" y2="31" stroke="#fff" stroke-width="1.3"/><line x1="34" y1="13" x2="34" y2="31" stroke="#fff" stroke-width="1.3"/></svg>
            <h3>Dinner</h3>
            A 2 course networking Dinner will be held at the Harbour Lane Restaurant, Launceston. Participants will be required to purchase their own drinks for this event.
          </div>
          <div class="info">
            <svg width="44" height="44" viewBox="0 0 44 44" aria-hidden="true"><circle cx="22" cy="22" r="20" fill="none" stroke="#fff" stroke-width="1.3"/><rect x="11" y="20" width="22" height="8" fill="none" stroke="#fff" stroke-width="1.3"/><rect x="14" y="15" width="7" height="5" fill="none" stroke="#fff" stroke-width="1.3"/><rect x="23" y="15" width="7" height="5" fill="none" stroke="#fff" stroke-width="1.3"/><line x1="12" y1="28" x2="12" y2="31" stroke="#fff" stroke-width="1.3"/><line x1="32" y1="28" x2="32" y2="31" stroke="#fff" stroke-width="1.3"/></svg>
            <h3>Accommodation</h3>
            Participants are welcome to choose their own accommodation. However, accommodation is available at The Riverbank Hotel starting at the special rate of $170.00 per night for participants in a One Bedroom Deluxe Suite.
          </div>
          <div class="info">
            <svg width="44" height="44" viewBox="0 0 44 44" aria-hidden="true"><circle cx="22" cy="22" r="20" fill="none" stroke="#fff" stroke-width="1.3"/><rect x="13" y="13" width="18" height="18" rx="2" fill="#fff"/><text x="22" y="27.5" text-anchor="middle" font-family="Montserrat, sans-serif" font-weight="700" font-size="14" fill="var(--forest-deep)">P</text></svg>
            <h3>Parking</h3>
            Limited parking is available at The Riverbank Hotel. Alternative parking is available at the car park located at 28 Quay Boulevard.
          </div>
          <div class="info">
            <svg width="44" height="44" viewBox="0 0 44 44" aria-hidden="true"><circle cx="22" cy="22" r="20" fill="none" stroke="#fff" stroke-width="1.3"/><text x="22" y="29" text-anchor="middle" font-family="Montserrat, sans-serif" font-weight="300" font-size="20" fill="#fff">?</text></svg>
            <h3>Enquiries</h3>
            If you have any enquiries about the <strong>Emerging Leaders Program</strong>, please contact Amelia Joyce at Civic Leaders Tasmania on 0400 000 123 or events@civicleaderstas.org.au
          </div>
        </div>
      </div>
    </article>
  </div>
</body>
</html>
```